New Product Catalogue

15-20 PAGE PRODUCT CATALOGUE
UPLOADED PDF YOUR ABLE TO EDIT AND GRAB IMAGES
SIZE OF CATALOGUE IS UP TO THE DESIGNER
WE WANT TO ADD FOR IMAGES AFTER THE INITAL DESIGN
VERY CREATIVE
WE WANT A NEW LOOK FOR CATALOGUE AND WE WANT IT TO LEAD ONTO OUR WEBSITE - WWW.KORVADISPLAY.COM.AU
WE ARE A EXHIBITION COMPANY AND WE VISUALLY NEED TO LOOK AMAZING PAGES MAY INCREASE SLIGHTLY AS WE HAVE SOME MORE FURNITURE PIECES TO ADD TO THE RANGE WHICH WILL PROVIDED TO THE WINNER.
Updates

Guys I appreciate the designs however we need to see the complete catalogue finished designing one page doesn't show us much. We want a complete redesign not just moving a few images around I am after a new layout who ever gets reward the job we will be supplying new images for them that are hi resolution.

Reason: We want to see better designs.

Hey Designers, We are extending the deadline so we have more people in the contest... Get creative we are looking at a complete new revamp of the catalogue. Which will then lead up to a new site.

Target Market(s)

CORPORATE CLIENTS ATTENDING TRADE SHOWS
WE WANT A MESSAGE TO LET THEM KNOW WE PRINT OVERNIGHT 24/7 - AS WE HAVE A PRINTING DIVISIONS

Industry/Entity Type

It Company

Font styles to use
Sans Serif

Requirements
Must have
• TELL THEM A STORY ABOUT OUR COMPANY - WE COVER EVERYTHING FOR THE TRADE SHOW - BOOTHS, FLOORING SOLUTIONS, FURNITURE HIRE - COUNTERS, ZENTABS, PLANTS HIRE, PULL UP BANNERS, PRINTING SOLUTIONS - FLYER'S BROCHURES - EVERYTHING YOU NEED FOR YOUR TRADE SHOW

```html
<!DOCTYPE html>
<html lang="en">
<head>
<meta charset="utf-8">
<title>Korva Catalogue Spreads</title>
<link rel="stylesheet" href="https://fonts.googleapis.com/css2?family=Montserrat:wght@400;600;700;800&family=Open+Sans:wght@400;600&display=swap">
<style>
  :root{
    --stage:#e9e6e1;
    --ink:#353642;
    --cyan:#00b5cf;
    --orange:#e8502a;
    --magenta:#b03a8c;
    --teal:#3aa9b0;
    --grey-type:#9a9aa5;
    --white:#ffffff;
    --yellow:#f6b818;
    --lime:#8cc63f;
    --green:#3daa4a;
    --coral:#ef5a5a;
    --amber:#f0822a;
  }
  *{margin:0;padding:0;box-sizing:border-box}
  html,body{width:1000px;height:1200px;overflow:hidden;background:var(--stage)}
  body{position:relative;font-family:"Montserrat",sans-serif;color:var(--ink)}
  .abs{position:absolute}
  .page-label{position:absolute;font-size:13px;color:var(--ink);font-family:"Open Sans",sans-serif;letter-spacing:.02em}
  .page{position:absolute;overflow:hidden;background:var(--white);box-shadow:0 2px 6px rgba(0,0,0,.25)}
  .placeholder{position:absolute}

  /* cover */
  .cover{left:25px;top:52px;width:467px;height:331px}
  .cover .spine{left:0;top:0;width:45px;height:100%;background:var(--ink)}
  .cover .cyan-panel{left:45px;top:0;width:167px;height:100%;background:var(--cyan)}
  .cover .headline{left:62px;top:122px;color:var(--white);font-weight:800;line-height:1}
  .cover .headline .big{font-size:31px;letter-spacing:.05em;display:block}
  .cover .headline .small{font-size:15.5px;letter-spacing:.06em;display:block;margin-top:3px;line-height:1.02}
  .cover .expo-tag{background:var(--orange);padding:0 3px}
  .cover .brand{right:12px;bottom:10px;display:flex;align-items:center;gap:5px;font-size:17px;font-weight:600;color:var(--cyan)}
  .dot{display:inline-block;width:14px;height:14px;border-radius:50%;background:var(--cyan)}

  /* intro */
  .intro{left:503px;top:52px;width:467px;height:331px}
  .intro .dark{left:0;top:0;width:240px;height:100%;background:var(--ink)}
  .intro h2{position:absolute;left:19px;top:109px;color:var(--white);font-size:16px;font-weight:700;letter-spacing:.03em}
  .intro .copy-box{left:18px;top:135px;width:245px;height:109px;background:var(--magenta);color:var(--white);font-size:8px;line-height:1.35;padding:22px 20px;text-transform:uppercase;font-family:"Open Sans",sans-serif}

  /* custom booths */
  .custom{left:25px;top:436px;width:467px;height:332px}
  .custom .dark{left:227px;top:0;width:240px;height:100%;background:var(--ink)}
  .custom .title{right:19px;top:73px;text-align:right;font-weight:700;font-size:15px;line-height:1.3;letter-spacing:.02em}
  .custom .title .w{color:var(--white);display:block}
  .custom .title .g{color:var(--grey-type);display:block}
  .custom .copy-box{left:200px;top:120px;width:248px;height:152px;background:var(--teal);color:var(--white);font-size:7.6px;line-height:1.45;padding:11px 12px;text-transform:uppercase;text-align:justify;font-family:"Open Sans",sans-serif}

  /* award */
  .award{left:503px;top:436px;width:469px;height:332px;background:var(--ink)}
  .award .title{left:25px;top:18px;font-weight:700;font-size:15px;line-height:1.1;letter-spacing:.02em;z-index:2}
  .award .g{color:var(--grey-type);display:block}
  .award .w{color:var(--white);display:block}
  .award .year{display:inline-block;background:var(--orange);color:var(--white);padding:0 8px 0 25px;margin:1px 0 1px -25px}
  .award .gallery{left:245px;top:0;width:224px;height:332px;background:var(--white)}

  /* upgrade */
  .upgrade{left:25px;top:813px;width:468px;height:331px}
  .upgrade .label{font-weight:800;font-size:12px;line-height:1;color:var(--ink);z-index:2}
  .upgrade .arrow{z-index:2}
  .upgrade .band{left:0;top:117px;width:100%;height:77px;background:var(--ink);color:var(--white)}
  .upgrade .band h3{position:absolute;left:20px;top:10px;font-size:16px;font-weight:800;letter-spacing:.03em}
  .upgrade .band .lead{position:absolute;left:20px;top:34px;width:200px;font-size:8px;line-height:1.4;font-weight:600;text-transform:uppercase}
  .upgrade .hl{color:var(--yellow)}
  .upgrade .band .legend{position:absolute;left:245px;top:32px;font-size:8px;line-height:1.5;font-weight:600;text-transform:uppercase}
  .key{display:inline-block;width:9px;height:9px;font-size:7px;line-height:9px;text-align:center;color:var(--white);margin-right:3px}
  .key.b{background:var(--green)}.key.r{background:var(--orange)}
  .upgrade .thumbs{left:0;top:194px;width:100%;height:86px}
  .thumb{position:absolute;top:6px;width:78px;height:68px}
  .thumb .keys{position:absolute;right:0;bottom:-10px;display:flex}
  .thumb .keys .key{margin:0 0 0 1px}
  .upgrade .footer{left:0;top:280px;width:100%;height:51px;background:var(--yellow);font-size:7.6px;line-height:1.3;font-weight:700;padding:5px 16px;text-transform:uppercase;color:var(--ink)}
  .upgrade .footer .mark{background:#1d3f8f;color:var(--white);padding:0 2px}

  /* back */
  .back{left:505px;top:813px;width:472px;height:331px}
  .back .dark{left:303px;top:0;width:169px;height:100%;background:var(--ink)}
  .city{position:absolute;left:0;height:25px;color:var(--white);font-weight:800;font-size:19px;line-height:25px;padding:0 8px 0 73px;letter-spacing:.03em;white-space:nowrap}
  .back .brand{left:345px;top:196px;display:flex;align-items:center;gap:6px;font-size:24px;font-weight:600;color:var(--cyan)}
  .back .phone{left:333px;top:254px;font-size:16px;font-weight:800;color:var(--lime)}
  .back .web{left:322px;top:273px;font-size:12.5px;font-weight:600;color:#7fd3e2}
</style>
</head>
<body>

<!-- Cover -->
<span class="page-label" style="left:25px;top:32px">COVER</span>
<section class="page cover">
  <div class="abs spine"></div>
  <div class="abs cyan-panel"></div>
  <h1 class="abs headline">
    <span class="big">WE ARE</span>
    <span class="small">THE COMPLETE<br>SOLUTION FOR<br>YOUR <span class="expo-tag">EXPO</span></span>
  </h1>
  <div class="placeholder" role="img" aria-label="Abstract faceted polygon burst in teal, magenta and gold" style="left:235px;top:18px;width:215px;height:280px;background:radial-gradient(ellipse at 50% 50%,#c8467e 0%,#6fa9b8 45%,rgba(255,255,255,0) 72%)"></div>
  <div class="abs brand"><span class="dot"></span>korva</div>
</section>

<!-- 01 Introduction -->
<span class="page-label" style="left:503px;top:32px">01</span>
<section class="page intro">
  <div class="abs dark"></div>
  <h2>INTRODUCTION</h2>
  <p class="abs copy-box">We are dedicated + motivated when it comes<br>to fast overnight printing<br>and providing you a<br>cost effective<br>solution for your tradeshow<br>or exhibition booth.</p>
  <div class="placeholder" role="img" aria-label="Folding display wall product" style="left:320px;top:30px;width:74px;height:70px;background:#a99ea9"></div>
  <div class="placeholder" role="img" aria-label="Lounge sofa hire" style="left:320px;top:103px;width:74px;height:62px;background:#c9d6d8"></div>
  <div class="placeholder" role="img" aria-label="Moulded chair hire" style="left:320px;top:168px;width:74px;height:55px;background:#f1f1f1"></div>
  <div class="placeholder" role="img" aria-label="Round cafe table hire" style="left:320px;top:227px;width:74px;height:72px;background:#d0cdd0"></div>
  <div class="placeholder" role="img" aria-label="Pull up banner product" style="left:397px;top:0;width:70px;height:68px;background:#a89aa4"></div>
  <div class="placeholder" role="img" aria-label="Tower display stand" style="left:397px;top:71px;width:70px;height:64px;background:#c7d3d5"></div>
  <div class="placeholder" role="img" aria-label="Shell scheme booth" style="left:397px;top:138px;width:70px;height:62px;background:#e8e0d6"></div>
  <div class="placeholder" role="img" aria-label="Curved backdrop wall" style="left:397px;top:204px;width:70px;height:60px;background:#d4d0d1"></div>
  <div class="placeholder" role="img" aria-label="Fabric counter" style="left:397px;top:268px;width:70px;height:63px;background:#e8dfe8"></div>
</section>

<!-- 02 Custom booths -->
<span class="page-label" style="left:25px;top:416px">02</span>
<section class="page custom">
  <div class="placeholder" role="img" aria-label="Custom built exhibition booth with shelving" style="left:18px;top:10px;width:190px;height:115px;background:linear-gradient(135deg,#e5e5e5,#c9cfc9)"></div>
  <div class="placeholder" role="img" aria-label="Circular hanging sign" style="left:55px;top:150px;width:110px;height:40px;background:linear-gradient(#eeeeee,#d6d6d6);border-radius:50%"></div>
  <div class="placeholder" role="img" aria-label="Booth display featuring a blue truck" style="left:18px;top:210px;width:200px;height:95px;background:linear-gradient(135deg,#3a6fb5,#b8b1a6)"></div>
  <div class="abs dark"></div>
  <h2 class="abs title"><span class="w">CUSTOM DESIGN</span><span class="g">EXHIBITION BOOTHS</span></h2>
  <p class="abs copy-box">Design &amp; build a stand that will stand out amongst your competitors and attract more customers to your stand, look no further, you have the right company on the job. Not only do we have years of knowledge and experience but we have a creative team like no other. We know what works and what doesn't therefore our design team work closely with you to ensure your exhibition booth looks unique and fantastic</p>
</section>

<!-- 03 Award -->
<span class="page-label" style="left:503px;top:416px">03</span>
<section class="page award">
  <div class="placeholder" role="img" aria-label="Dark faceted polygon shape in magenta and plum" style="left:20px;top:110px;width:170px;height:222px;background:radial-gradient(ellipse at 45% 50%,#6b2f5c 0%,#4a3a50 45%,rgba(53,54,66,0) 75%)"></div>
  <div class="placeholder" role="img" aria-label="Award plaque" style="left:190px;top:77px;width:52px;height:53px;background:#ffffff"><div style="margin:8px;width:36px;height:36px;background:#2a2b31"></div></div>
  <h2 class="abs title">
    <span class="g">AWARDED THE BEST</span>
    <span class="g">EXHIBITION BOOTH</span>
    <span class="w">1-4 SEPTEMBER</span>
    <span class="w"><span class="year">2013</span></span>
    <span class="w">TERRA EXPO</span>
  </h2>
  <div class="abs gallery"></div>
  <div class="placeholder" role="img" aria-label="Award winning booth with orange arch" style="left:255px;top:10px;width:205px;height:130px;background:linear-gradient(135deg,#e59a2c,#2d6aa8 60%,#6b5236)"></div>
  <div class="placeholder" role="img" aria-label="White walled booth interior" style="left:248px;top:145px;width:160px;height:100px;background:linear-gradient(135deg,#d9ddd9,#b8c2bd)"></div>
  <div class="placeholder" role="img" aria-label="Blue and white corner booth" style="left:330px;top:220px;width:130px;height:105px;background:linear-gradient(135deg,#2f8fc9,#e8e8e8)"></div>
</section>

<!-- 04 Upgrade options -->
<span class="page-label" style="left:25px;top:795px">04</span>
<section class="page upgrade">
  <div class="placeholder" role="img" aria-label="Empty shell scheme booth" style="left:30px;top:44px;width:98px;height:66px;background:linear-gradient(#f2f2f2,#d0d0d0)"></div>
  <div class="placeholder" role="img" aria-label="Upgraded booth with green graphics" style="left:190px;top:40px;width:95px;height:71px;background:linear-gradient(135deg,#3e8a4f,#cfd8cf)"></div>
  <div class="placeholder" role="img" aria-label="Upgraded booth with leafy backdrop" style="left:345px;top:30px;width:95px;height:80px;background:linear-gradient(135deg,#5d8a3a,#e0e4d8)"></div>

  <span class="abs label" style="left:65px;top:25px">FROM</span>
  <svg class="abs arrow" style="left:100px;top:20px" width="18" height="24" viewBox="0 0 18 24"><path d="M2 2 Q12 4 12 14 M7 11 L12 18 L16 10" fill="none" stroke="#00b5cf" stroke-width="3"/></svg>
  <span class="abs label" style="left:170px;top:10px">CONVERT<br>TO THIS</span>
  <svg class="abs arrow" style="left:228px;top:10px" width="16" height="22" viewBox="0 0 16 22"><path d="M8 0 V16 M2 10 L8 18 L14 10" fill="none" stroke="#00b5cf" stroke-width="3"/></svg>
  <span class="abs label" style="left:310px;top:84px">OR</span>
  <svg class="abs arrow" style="left:330px;top:70px" width="18" height="18" viewBox="0 0 18 18"><path d="M2 16 L14 4 M6 3 H15 V12" fill="none" stroke="#00b5cf" stroke-width="3"/></svg>

  <div class="abs band">
    <h3>3X3 UPGRADE OPTIONS</h3>
    <p class="lead"><span class="hl">Don't look like the shell!</span> Stand out and be seen <span class="hl">now!</span><br>Without breaking the budget.</p>
    <p class="legend"><span class="key b">B</span><span style="color:#8cc63f">Buy &amp; self install</span> or get cost to install<br><span class="key r">R</span><span style="color:#f08a3c">Rental</span> bundlled with furniture</p>
  </div>

  <div class="abs thumbs">
    <div class="thumb" role="img" aria-label="Option 1 printed booth" style="left:18px;background:linear-gradient(135deg,#e45b2a,#f2f2f2)"><div class="keys"><span class="key r">R</span><span class="key b">B</span></div></div>
    <div class="thumb" role="img" aria-label="Option 2 fabric walls" style="left:103px;background:linear-gradient(135deg,#c9302c,#f2f2f2)"><div class="keys"><span class="key b">B</span><span class="key r">R</span></div></div>
    <div class="thumb" role="img" aria-label="Option 3 pop up display walls" style="left:188px;background:linear-gradient(135deg,#2e5aa8,#f2f2f2)"><div class="keys"><span class="key b">B</span></div></div>
    <div class="thumb" role="img" aria-label="Option 4 customised fabric wall" style="left:275px;background:linear-gradient(135deg,#1f3d7a,#f2f2f2)"><div class="keys"><span class="key r">R</span><span class="key b">B</span></div></div>
    <div class="thumb" role="img" aria-label="Option 5 portable fabric wall" style="left:362px;background:linear-gradient(135deg,#3a3a3a,#b5c94a 60%,#f2f2f2)"><div class="keys"><span class="key b">B</span></div></div>
  </div>

  <p class="abs footer">1. Printed 2. Fabric walls (3m x 2.4m) *Does not require shell scheme<br>2. Fabric walls not using shell scheme<br>3. Curve or straight pop up display walls 4. Customised<br>portable fabric wall created to <span class="mark">stand out</span> 5. Fabric portable wal</p>
</section>

<!-- Back -->
<span class="page-label" style="left:505px;top:795px">BACK</span>
<section class="page back">
  <div class="placeholder" role="img" aria-label="Soft faceted polygon pattern in pastel pink, lilac and grey" style="left:0;top:0;width:303px;height:331px;background:linear-gradient(135deg,#efe7ea 0%,#d9c4d0 40%,#f3eef0 70%,#c9c2cb 100%)"></div>
  <div class="abs dark"></div>
  <div class="city" style="top:102px;min-width:173px;background:var(--amber)">SYDNEY</div>
  <div class="city" style="top:132px;min-width:225px;background:var(--cyan)">MELBOURNE</div>
  <div class="city" style="top:162px;min-width:198px;background:var(--magenta)">BRISBANE</div>
  <div class="city" style="top:191px;min-width:187px;background:var(--green)">ADELAIDE</div>
  <div class="city" style="top:221px;min-width:157px;background:var(--coral)">PERTH</div>
  <div class="abs brand"><span class="dot" style="width:18px;height:18px"></span>korva</div>
  <div class="abs phone">1300 555 018</div>
  <div class="abs web">korvadisplay.com.au</div>
</section>

</body>
</html>
```